Etiketten für Fruchtaufstriche eines Hofladens
Zielgruppe
Wir sind der Lindqvisthof Hofladen (www.lindqvisthof-beispiel.de), ein regionaler Erzeuger und Händler hochwertiger Lebensmittel. Für unsere hausgemachten Fruchtaufstriche suchen wir ein neues schönes Etikett das auch hochwertig wirkt. Die Produkte sind eher hochpreisig und hochwertig. Das Etikett sollte daher auch nicht irgendwie 'billig' wirken.
Aufgabenstellung
Wie bereits schon erwähnt, sollte das Etikett hochwertig wirken. Als Endformat stellen wir uns eine Breite von 95mm und eine Höhe von 60mm vor. Siehe hierzu die Vorlage der Druckerei im Anhang (bitte Beschnitt von 6mm beachten). Es wird ein ganz normales rundes Glas verwendet.
Bitte beachten Sie, dass wir kein industrieller Hersteller sind sondern eine kleine Manufaktur. Damit die verschiedenen Sorten einfach zu erkennen sind, wäre beispielsweise eine Erdbeere (farbig) auf schön. Bei anderen Sorten, wie beispielsweise bei einem Himbeer Fruchtaufstrich, gegen eine Himbeere ausgetauscht werden. Das Etikett sollte später auch anpassbar sein, immer wieder ändern sich Vorschriften zur Deklaration, diese wollen wir selbst einfach anpassen können. Außerdem soll das Etikett in Zukunft auch einfach und spontan auf weitere Sorten Fruchtaufstrich anpassbar sein, hierzu müssen wir selbst die Zutatenliste und natürlich den Titel ändern können. Deshalb ist es wichtig, dass wir am Ende ein InDesign Format zur Verfügung haben.
Was soll auf das Etikett:
Bezeichnung:
Erdbeer Fruchtaufstrich
Hersteller:
Lindqvisthof Hofladen GbR
Bernd und Carola Wessling
Obere Kastanienallee 17
83719 Rainfeld
Logo:
siehe Datei
Inhalt:
275ml
Zutaten:
Erdbeeren, Gelierzucker 2:1, Zitronensäure
Haltbarkeit:
mindestens haltbar bis: siehe Boden
Internetadresse:
www.lindqvisthof-beispiel.de

```html
<!DOCTYPE html>
<html lang="de">
<head>
<meta charset="utf-8">
<title>Etikett Erdbeer Fruchtaufstrich – Lindqvisthof Hofladen</title>
<link rel="stylesheet" href="https://fonts.googleapis.com/css2?family=Dancing+Script:wght@700&family=Open+Sans:wght@400;600;700&display=swap">
<style>
  :root {
    --page-bg: #ecebe8;
    --wood-dark: #2b2d30;
    --wood-mid: #43464a;
    --wood-light: #55585d;
    --band-red: #d8141c;
    --base-black: #141414;
    --text-white: #ffffff;
    --text-soft: #c9c9c9;
    --leaf-green: #5f9e5a;
    --berry-red: #d62a2a;
    --logo-green: #4e9a3a;
  }
  * { margin: 0; padding: 0; box-sizing: border-box; }
  html, body {
    width: 1200px; height: 1030px; overflow: hidden;
    background: var(--page-bg);
    font-family: "Open Sans", Arial, sans-serif;
  }
  .canvas { position: relative; width: 1200px; height: 1030px; }
  .label {
    position: absolute; left: 50px; top: 165px;
    width: 1100px; height: 700px;
    display: flex; flex-direction: column;
    box-shadow: 0 6px 24px rgba(0,0,0,.18);
    overflow: hidden;
  }
  .label__top {
    position: relative; height: 440px;
    background: linear-gradient(100deg, var(--wood-dark) 0%, var(--wood-mid) 35%, var(--wood-light) 55%, var(--wood-mid) 75%, var(--wood-dark) 100%);
  }
  .fruit-illustration {
    position: absolute; left: 50%; top: 40px; transform: translateX(-50%);
    width: 380px; height: 230px; border-radius: 50%;
    background: radial-gradient(ellipse at 50% 65%, var(--berry-red) 0%, #b81f22 45%, var(--leaf-green) 75%, rgba(95,158,90,0) 100%);
  }
  .brand {
    position: absolute; left: 0; right: 0; top: 300px;
    display: flex; align-items: center; justify-content: center; gap: 18px;
  }
  .brand__mark {
    width: 34px; height: 34px; border-radius: 50%;
    background: var(--logo-green);
  }
  .brand__name {
    font-family: "Open Sans", Arial, sans-serif;
    font-weight: 700; font-size: 58px; color: var(--logo-green);
    letter-spacing: 1px;
  }
  .label__band {
    height: 100px; background: var(--band-red);
    display: flex; align-items: center; justify-content: center;
  }
  .product-title {
    font-family: "Dancing Script", cursive;
    font-weight: 700; font-size: 68px; color: var(--text-white);
    line-height: 1;
  }
  .label__base {
    position: relative; flex: 1; background: var(--base-black);
    color: var(--text-white);
  }
  .website {
    position: absolute; left: 0; right: 0; top: 10px;
    text-align: center; font-size: 17px; color: var(--text-soft);
  }
  .declaration {
    position: absolute; top: 46px;
    font-size: 17px; line-height: 1.45; color: var(--text-soft);
  }
  .declaration--maker { left: 40px; }
  .declaration--product { right: 40px; width: 380px; }
  .declaration strong { font-weight: 600; color: var(--text-white); }
</style>
</head>
<body>
<main class="canvas">
  <section class="label">
    <div class="label__top" role="img" aria-label="Dunkle Holzmaserung als Hintergrund">
      <div class="fruit-illustration" role="img" aria-label="Illustration: drei rote Erdbeeren mit grünen Blättern"></div>
      <div class="brand">
        <span class="brand__mark"></span>
        <span class="brand__name">Lindqvisthof</span>
      </div>
    </div>
    <div class="label__band">
      <h1 class="product-title">Erdbeer Fruchtaufstrich</h1>
    </div>
    <div class="label__base">
      <p class="website">www.lindqvisthof-beispiel.de</p>
      <p class="declaration declaration--maker">
        <strong>Hersteller:</strong><br>
        Lindqvisthof Hofladen GbR<br>
        Bernd und Carola Wessling<br>
        Obere Kastanienallee 17, 83719 Rainfeld
      </p>
      <p class="declaration declaration--product">
        <strong>Zutaten:</strong> Erdbeeren, Gelierzucker 2:1, Zitronensäure<br>
        <strong>Inhalt:</strong> 275ml<br>
        mindestens haltbar bis: siehe Boden
      </p>
    </div>
  </section>
</main>
</body>
</html>
```